Design Professional Car Wrap for Lawyer

I need a 1/2 wrap design for my law firm. I want the colors to be consistent with our branding. The design must be professional and look very sharp. The car is a 2012 Marvondel Pelta Hatchback Black. I want the logo and slogan to be used throughout the design and you can incorporate my picture on the car as well. Please brand the car similar to our logo, letterhead, business card and banners to keep our image consistent. I have included some pictures of wraps that I like for inspiration. I also have included a black pelta car so you can provide mockups. The completed project will need to be print ready files and design files. Please include our website url on the wrap, however I do not want it to be a large part of the design. Also include the Grouvely Logo and Tiepoint logo. You can include our phone number as well if you want, but its not necessary.

Slogan is "LAWYER UP"

```html
<!DOCTYPE html>
<html lang="en">
<head>
<meta charset="utf-8">
<title>Penwick Law Group – Vehicle Wrap Panel</title>
<link rel="stylesheet" href="https://fonts.googleapis.com/css2?family=Tinos:wght@400;700&display=swap">
<style>
  :root {
    --backdrop: #e6e6e6;
    --panel: #3b3634;
    --swoosh: #3aa7dc;
    --ink: #ffffff;
    --ink-soft: #e8e8e8;
    --portrait-top: #6e7d93;
    --portrait-bottom: #2c3650;
  }
  html, body {
    margin: 0;
    padding: 0;
    width: 1200px;
    height: 675px;
    overflow: hidden;
    background: var(--backdrop);
  }
  .wrap-panel {
    display: block;
    width: 1200px;
    height: 675px;
    font-family: "Tinos", "Times New Roman", serif;
  }
  .panel-body { fill: var(--panel); }
  .swoosh { fill: none; stroke: var(--swoosh); stroke-linecap: round; }
  .logo-frame { fill: none; stroke: var(--ink); stroke-width: 3; }
  .logo-name { fill: var(--ink); font-size: 30px; font-weight: 700; letter-spacing: 1px; }
  .firm-name { fill: var(--ink); font-size: 46px; }
  .firm-type { fill: var(--ink-soft); font-size: 36px; }
  .slogan { fill: var(--ink); font-size: 68px; }
  .offices-label { fill: var(--ink); font-size: 44px; }
  .office { fill: var(--ink); font-size: 32px; letter-spacing: 1px; }
  .phone { fill: var(--ink); font-size: 46px; }
  .phone-icon { fill: var(--ink); }
  .website { fill: var(--ink); font-size: 30px; }
  .social-name { fill: var(--ink); font-size: 20px; font-weight: 700; }
  .social-dot { fill: var(--swoosh); }
</style>
</head>
<body>
<svg class="wrap-panel" viewBox="0 0 1200 675" xmlns="http://www.w3.org/2000/svg">
  <defs>
    <linearGradient id="portrait-tone" x1="0" y1="0" x2="0" y2="1">
      <stop offset="0" stop-color="var(--portrait-top)"/>
      <stop offset="1" stop-color="var(--portrait-bottom)"/>
    </linearGradient>
  </defs>

  <path class="panel-body" d="M60,60 H1040 Q1140,60 1140,170 V510 Q1140,620 1030,620 H60 Z"/>

  <rect x="560" y="335" width="150" height="255" rx="6" fill="url(#portrait-tone)"
        role="img" aria-label="Portrait photo of the attorney in suit and red tie"/>

  <path class="swoosh" stroke-width="16" d="M790,66 Q560,230 430,570"/>
  <path class="swoosh" stroke-width="12" d="M440,615 Q700,500 1000,560"/>

  <rect class="logo-frame" x="72" y="72" width="40" height="40"/>
  <text class="logo-name" x="124" y="104">PENWICK</text>

  <text class="firm-name" x="72" y="250" textLength="440" lengthAdjust="spacingAndGlyphs">GARETH L. PENWICK</text>
  <text class="firm-type" x="148" y="306">Law Group PLLC</text>

  <text class="slogan" x="768" y="178" textLength="350" lengthAdjust="spacingAndGlyphs">LAWYER UP</text>
  <text class="offices-label" x="770" y="245">OFFICES:</text>
  <text class="office" x="770" y="300">ASHBURY</text>
  <text class="office" x="770" y="355">FENWICK RIDGE</text>

  <path class="phone-icon" d="M790,380 q-14,8 -8,30 q8,24 26,34 q10,4 16,-4 l-10,-12 q-6,4 -10,-2 q-8,-10 -10,-20 q0,-6 6,-6 z"/>
  <text class="phone" x="838" y="428" textLength="280" lengthAdjust="spacingAndGlyphs">(555)014-0187</text>

  <text class="website" x="560" y="596">www.glp-law.com</text>
  <circle class="social-dot" cx="826" cy="588" r="7"/>
  <text class="social-name" x="838" y="595">Grouvely</text>
  <text class="social-name" x="930" y="595">Tiepoint</text>
</svg>
</body>
</html>
```